Business Card for Wholesale Comapany
Pelvo Goods
Business Card for Wholesale Comapany - Construction
Creative Brief
Professional
Mark Tilney
Chief Sales Officer
8142-C Marlow Ridge Boulevard #310 Houston, TX. 77031-2287
mtilney@pelvogoods.example
www.pelvogoods.example
Your design can be for one or both sides of the card, I do not have a preference. I just completed the contest for my logo design and as soon as the .ai file is sent to me I will forward. But, for the time being, you can find my logo at http://www.brakenstudio.example/drafts/display/contest/519274/draft/7a1c04be92d3f65e08b1c7a94f3e2d60b815937.
rkanto41q rkanto41q
Here is the .ai file for the logo, so hopefully this will make it easier for you designs. Also, some great designs have been submitted and here are some items I have gravitated to: 1. I am going to want rounded corners. 2. I like the idea of having a 2 sided card. 3. On the back, almost all designs have come in black. I would like to see another color used, or make a statement with design on a white background. 4. Don't be too heavily skewed to the professional type of card. Thanks
VelMar VelMar
What font did you use sir?

```html
<!DOCTYPE html>
<html lang="en">
<head>
<meta charset="utf-8">
<title>Pelvo Goods – Business Card</title>
<link rel="stylesheet" href="https://fonts.googleapis.com/css2?family=Roboto:wght@300;400;700&display=swap">
<style>
  :root {
    --bg-top: #d9d9d9;
    --bg-bottom: #b3b3b3;
    --card: #ffffff;
    --gold: #c49a5a;
    --tan: #c9a36c;
    --tan-dark: #8a6a3e;
    --slate: #8e8e8e;
    --ink: #3b3b3b;
    --ink-soft: #5a5a5a;
  }
  * { box-sizing: border-box; margin: 0; padding: 0; }
  html, body { width: 1200px; height: 908px; overflow: hidden; }
  body {
    background: linear-gradient(180deg, var(--bg-top), var(--bg-bottom));
    font-family: "Roboto", Arial, sans-serif;
    color: var(--ink);
    position: relative;
  }
  .card {
    position: absolute;
    left: 300px;
    width: 600px;
    height: 343px;
    background: var(--card);
    border-radius: 14px;
    overflow: hidden;
    box-shadow: 0 10px 24px rgba(0,0,0,.22);
  }
  .card--front { top: 78px; }
  .card--back { top: 481px; }

  /* Front */
  .front-frame {
    position: absolute;
    inset: 26px;
    border: 3px solid var(--gold);
  }
  .wordmark {
    display: flex;
    align-items: center;
    gap: 12px;
    font-weight: 700;
    color: var(--gold);
    white-space: nowrap;
  }
  .wordmark__mark {
    background: var(--tan-dark);
    flex: none;
  }
  .card--front .wordmark {
    position: absolute;
    left: 50%; top: 50%;
    transform: translate(-50%, -50%);
    font-size: 46px;
  }
  .card--front .wordmark__mark { width: 46px; height: 46px; }

  /* Back */
  .card--back .wordmark {
    position: absolute;
    left: 34px; top: 44px;
    font-size: 32px;
    gap: 10px;
  }
  .card--back .wordmark__mark { width: 32px; height: 32px; }
  .name-block {
    position: absolute;
    right: 0; top: 36px;
    width: 250px; height: 70px;
    background: var(--slate);
    color: #fff;
    padding: 12px 20px;
  }
  .name-block__name {
    font-size: 21px;
    font-weight: 700;
    letter-spacing: 1px;
    text-transform: uppercase;
    white-space: nowrap;
  }
  .name-block__title {
    font-size: 14px;
    font-weight: 300;
    margin-top: 3px;
  }
  .contacts, .icons {
    position: absolute;
    left: 34px; right: 22px;
    display: grid;
    grid-template-columns: 112px 176px 1fr;
    column-gap: 18px;
  }
  .contacts {
    top: 140px;
    font-size: 12px;
    line-height: 1.6;
    color: var(--ink-soft);
    white-space: nowrap;
  }
  .rule {
    position: absolute;
    left: 0; right: 0; top: 254px;
    height: 2px;
    background: var(--tan-dark);
  }
  .icons { top: 239px; }
  .icons svg { width: 32px; height: 32px; display: block; }
  .band {
    position: absolute;
    left: 0; right: 0; bottom: 0;
    height: 62px;
    background: var(--tan);
  }
</style>
</head>
<body>
  <section class="card card--front" aria-label="Card front">
    <div class="front-frame"></div>
    <div class="wordmark"><span class="wordmark__mark"></span>Pelvo Goods</div>
  </section>

  <section class="card card--back" aria-label="Card back">
    <div class="wordmark"><span class="wordmark__mark"></span>Pelvo Goods</div>
    <div class="name-block">
      <div class="name-block__name">Mark Tilney</div>
      <div class="name-block__title">Managing Director</div>
    </div>
    <div class="contacts">
      <p class="contacts__item">014 268 3957<br>014 268 3958</p>
      <p class="contacts__item">mtilney@pelvogoods.example<br>www.pelvogoods.example</p>
      <p class="contacts__item">8142-C Marlow Ridge Boulevard #310<br>Houston, TX. 77031-2287</p>
    </div>
    <div class="rule"></div>
    <div class="icons">
      <div class="icons__slot">
        <svg viewBox="0 0 32 32" aria-label="Phone"><circle cx="16" cy="16" r="15" fill="#3b3b3b"/><path d="M11 9h3l1.5 4-2 1.5a9 9 0 0 0 4 4l1.5-2 4 1.5v3c0 1-1 2-2 2A13 13 0 0 1 9 11c0-1 1-2 2-2z" fill="#fff"/></svg>
      </div>
      <div class="icons__slot">
        <svg viewBox="0 0 32 32" aria-label="Web"><circle cx="16" cy="16" r="15" fill="#3b3b3b"/><g fill="none" stroke="#fff" stroke-width="1.5"><circle cx="16" cy="16" r="8"/><ellipse cx="16" cy="16" rx="3.5" ry="8"/><path d="M8 16h16M9.5 12h13M9.5 20h13"/></g></svg>
      </div>
      <div class="icons__slot">
        <svg viewBox="0 0 32 32" aria-label="Location"><circle cx="16" cy="16" r="15" fill="#3b3b3b"/><path d="M16 8a5.5 5.5 0 0 0-5.5 5.5C10.5 18 16 24 16 24s5.5-6 5.5-10.5A5.5 5.5 0 0 0 16 8z" fill="#fff"/><circle cx="16" cy="13.5" r="2" fill="#3b3b3b"/></svg>
      </div>
    </div>
    <div class="band"></div>
  </section>
</body>
</html>
```